Tavorly - Landing Page

Need a landing page for a journal app. The app is based on a retrospective board, where each journal entry is split into 3 sections: "What went well", "What Didn't Go Well" and "Things To Try".
The landing page should match the style of all modern web application landing pages. Think Brimo, Quenta, Vexadro. I've included screenshots of the app.
One feature that I want to highlight that is not ready yet, is an AI coach. It will offer insights based on the history of the user's journal entries
1 page

```html
<!DOCTYPE html>
<html lang="en">
<head>
<meta charset="utf-8">
<title>Tavorly – Journal App</title>
<link href="https://fonts.googleapis.com/css2?family=Kanit:wght@500;600&family=Urbanist:wght@400;500;600;700&display=swap" rel="stylesheet">
<style>
:root{
  --lime:#dcfc62;
  --lime-btn:#cdee5c;
  --lime-text:#c3e553;
  --lime-shadow:#3d4a18;
  --navy:#2d3447;
  --navy-deep:#252d40;
  --ink:#1c2130;
  --grey:#8a8f99;
  --app-bg:#e6e7ea;
  --app-line:#d0d2d7;
  --app-field:#ecedef;
  --green:#4caf76;
  --white:#ffffff;
}
*{box-sizing:border-box;margin:0;padding:0}
html,body{width:1200px;height:3015px;overflow:hidden;background:var(--white)}
body{position:relative;font-family:"Urbanist",sans-serif;color:var(--ink)}
.abs{position:absolute}
.topbar{position:absolute;left:0;top:0;width:1200px;height:7px;background:var(--lime-btn)}
.logo{position:absolute;font-family:"Urbanist",sans-serif;font-weight:600;font-size:29px;color:var(--ink);letter-spacing:-.2px}
.nav{position:absolute;top:24px;left:240px;display:flex;align-items:center;height:31px;font-size:15px;font-weight:500}
.nav a{color:var(--ink);text-decoration:none;position:absolute;white-space:nowrap}
.nav .is-active{background:var(--lime);border-radius:16px;padding:6px 12px;top:0;left:0}
.btn{position:absolute;display:flex;align-items:center;justify-content:center;background:var(--lime-btn);color:var(--ink);font-weight:600;border-radius:20px;box-shadow:0 3px 0 var(--lime-shadow);font-size:17px}
.hero-title{position:absolute;left:0;width:1200px;top:115px;text-align:center;font-weight:600;font-size:27px;line-height:35px}
.hero-title .accent{color:var(--lime-text)}
.hero-text{position:absolute;left:0;width:1200px;top:203px;text-align:center;color:var(--grey);font-size:16.5px;line-height:23px}
.band{position:absolute;left:0;top:540px;width:1200px;height:1940px}

/* app board */
.board{position:absolute;width:926px;height:489px;border-radius:26px;background:var(--app-bg);overflow:hidden;transform-origin:0 0}
.board--white{background:var(--white);border-radius:0}
.board__side{position:absolute;left:0;top:0;bottom:0;width:64px;background:var(--navy-deep)}
.board__mark{position:absolute;left:26px;top:8px;width:13px;height:13px;background:var(--lime-btn);border-radius:2px}
.board__icon{position:absolute;left:26px;width:13px;height:10px;border:1.5px solid #cfd3dc;border-radius:2px}
.board__icon--on{left:20px;width:25px;height:16px;background:#3a4358;border:none;border-radius:3px}
.board__icon--on::after{content:"";position:absolute;left:7px;top:4px;width:11px;height:8px;border:1.5px solid #e4e7ee;border-radius:1px}
.board__avatar{position:absolute;left:20px;bottom:7px;width:24px;height:24px;border-radius:50%;background:#c9ced8}
.board__title{position:absolute;left:125px;top:10px;font-family:Arial,sans-serif;font-weight:700;font-size:15px;color:#2a2e36}
.board__date{position:absolute;left:129px;top:43px;font-family:Arial,sans-serif;font-size:10px;color:#333;display:flex;align-items:center;gap:6px}
.board__date::before{content:"";width:8px;height:8px;border:1.5px solid #555;border-radius:1px}
.pill{display:inline-block;background:var(--green);color:#fff;font-family:Arial,sans-serif;font-size:8.5px;padding:3px 10px;border-radius:10px}
.board__tag{position:absolute;left:242px;top:39px;box-shadow:0 0 0 2px #bfe6cd}
.col{position:absolute;top:80px;width:221px;height:383px;border:1px solid var(--app-line);background:#e9eaec;border-radius:3px}
.board--white .col{background:#fafafa}
.col__head{position:absolute;left:11px;top:11px;font-family:Arial,sans-serif;font-size:9px;color:#333;display:flex;align-items:center;gap:9px}
.col__icon{width:9px;height:9px;background:#3f6fd6;border-radius:2px}
.col__icon--tri{background:none;width:0;height:0;border-left:5px solid transparent;border-right:5px solid transparent;border-bottom:9px solid #3f6fd6;border-radius:0}
.col__editor{position:absolute;left:7px;right:7px;top:38px;bottom:9px;border:1px solid var(--app-line);background:#dcdde0}
.board--white .col__editor{background:#f1f1f2}
.col__tools{position:absolute;left:8px;top:6px;font-family:Arial,sans-serif;font-size:8px;color:#333;line-height:15px;letter-spacing:.5px}
.col__tools b{margin-left:18px}
.col__body{position:absolute;left:7px;right:7px;top:42px;bottom:8px;background:var(--app-field);border:1px solid var(--app-line)}
.board--white .col__body{background:#fff}
.col__body ul{list-style:none;padding:12px 10px 0 14px;font-family:Arial,sans-serif;font-size:10.3px;line-height:15px;color:#222}
.col__body li{position:relative;padding-left:7px}
.col__body li::before{content:"•";position:absolute;left:0}

/* list view */
.list-shot{position:absolute;left:107px;top:1986px;width:473px;height:269px;background:#fff;overflow:hidden}
.list-shot .side{position:absolute;left:0;top:0;bottom:0;width:19px;background:var(--navy-deep)}
.list-shot .side i{position:absolute;left:6px;width:7px;height:5px;border:1px solid #cfd3dc}
.list-shot .add{position:absolute;left:54px;top:23px;border:1px solid #bbb;border-radius:3px;font-size:6px;font-weight:600;padding:2px 6px;font-family:Arial,sans-serif}
.list-shot .gym{position:absolute;left:416px;top:24px;font-size:5px;padding:2px 6px}
.entry{position:absolute;left:54px;width:380px;border:1px solid #e2e2e2;border-radius:3px;padding:7px 8px;font-family:Arial,sans-serif;font-size:5px;line-height:7.5px;color:#333}
.entry h4{font-size:6.2px;margin-bottom:2px}
.entry em{font-style:normal;color:#999;display:block}

/* features */
.card{position:absolute;width:459px;height:357px;background:var(--lime);border-radius:46px}
.feature-title{position:absolute;font-family:"Kanit",sans-serif;font-weight:600;font-size:45px;line-height:50px;color:var(--white);white-space:nowrap}
.rule{position:absolute;height:4px;width:97px;background:var(--lime-btn)}
.feature-text{position:absolute;width:432px;font-weight:500;font-size:16.8px;line-height:34.3px;color:var(--white)}
.connector{position:absolute;left:0;top:0}

.ai-title{position:absolute;left:0;width:1200px;top:2535px;text-align:center;font-family:"Kanit",sans-serif;font-weight:600;font-size:52px;line-height:60px;color:var(--ink)}
.ai-text{position:absolute;left:150px;width:900px;top:2638px;text-align:center;color:var(--grey);font-size:20.5px;line-height:34.5px;font-weight:500}
.footer-line{position:absolute;left:98px;top:2858px;width:1002px;height:1px;background:#cfd2d8}
.footer-nav{position:absolute;top:2894px;font-size:21px;font-weight:500;color:var(--ink)}
.copyright{position:absolute;right:100px;top:2933px;font-size:21px;font-weight:500;color:var(--ink)}
</style>
</head>
<body>

<div class="topbar"></div>
<div class="logo" style="left:98px;top:20px">Tavorly</div>
<nav class="nav">
  <a class="is-active">Features</a>
  <a style="left:117px;top:6px">Solutions</a>
  <a style="left:227px;top:6px">Enterprise</a>
  <a style="left:343px;top:6px">Resources</a>
  <a style="left:458px;top:6px">Pricing</a>
  <a style="left:661px;top:6px">Sign in</a>
</nav>
<a class="btn" style="left:967px;top:23px;width:133px;height:36px">Get Started</a>

<h1 class="hero-title"><span class="accent">Are You Looking For Recommendations For A</span> Journal App Or Some<br>Tips On How To Use One Effectively?</h1>
<p class="hero-text">Lorem ipsum dolor sit amet, consectetur adipiscing elit, sed do eiusmod tempor<br>incididunt ut labore et dolore magna aliqua.</p>
<a class="btn" style="left:533px;top:262px;width:133px;height:37px">Start for free</a>

<svg class="band" viewBox="0 0 1200 1940" role="img" aria-label="Dark blue toned photo of an open journal and pen on a desk">
  <defs>
    <linearGradient id="bandFill" x1="0" y1="0" x2="0.3" y2="1">
      <stop offset="0" stop-color="#2b3245"/>
      <stop offset="0.35" stop-color="#3b4458"/>
      <stop offset="0.7" stop-color="#353d51"/>
      <stop offset="1" stop-color="#2b3245"/>
    </linearGradient>
  </defs>
  <path d="M0,50 C60,20 120,5 200,5 L1000,5 C1080,5 1150,15 1200,30 L1200,1850 C1120,1865 1050,1930 960,1930 C820,1930 720,1822 560,1822 C400,1822 200,1880 0,1890 Z" fill="url(#bandFill)"/>
</svg>

<!-- hero board -->
<div class="board" style="left:137px;top:337px">
  <div class="board__side">
    <span class="board__mark"></span>
    <span class="board__icon board__icon--on" style="top:43px"></span>
    <span class="board__icon" style="top:70px"></span>
    <span class="board__icon" style="top:93px"></span>
    <span class="board__avatar"></span>
  </div>
  <div class="board__title">Entry</div>
  <div class="board__date">Thu Aug 22 2024 ⌄</div>
  <span class="pill board__tag">Gym</span>
  <div class="col" style="left:125px">
    <div class="col__head"><span class="col__icon"></span>What Went Well?</div>
    <div class="col__editor"><div class="col__tools">Normal &nbsp;⇕ <b>B</b> <i>I</i> U S ”<br>☰ ☰ ☰ ☰ &nbsp;&nbsp;T</div>
      <div class="col__body"><ul><li>Completed all scheduled workouts this week.</li><li>Increased bench press weight by 10 pounds.</li><li>Maintained consistent energy levels throughout sessions.</li></ul></div></div>
  </div>
  <div class="col" style="left:375px">
    <div class="col__head"><span class="col__icon col__icon--tri"></span>What Didn't Go Well?</div>
    <div class="col__editor"><div class="col__tools">Normal &nbsp;⇕ <b>B</b> <i>I</i> U S ”<br>☰ ☰ ☰ ☰ &nbsp;&nbsp;T</div>
      <div class="col__body"><ul><li>Struggled with form on deadlifts, leading to lower back discomfort.</li><li>Missed two stretching sessions after workouts.</li><li>Skipped meal prep, resulting in inconsistent nutrition.</li></ul></div></div>
  </div>
  <div class="col" style="left:624px">
    <div class="col__head"><span class="col__icon"></span>Things To Try</div>
    <div class="col__editor"><div class="col__tools">Normal &nbsp;⇕ <b>B</b> <i>I</i> U S ”<br>☰ ☰ ☰ ☰ &nbsp;&nbsp;T</div>
      <div class="col__body"><ul><li>Focus on deadlift form by lowering the weight and reviewing proper technique.</li><li>Set reminders for post-workout stretching to prevent muscle tightness.</li><li>Dedicate Sunday evenings to meal prep to ensure a balanced diet.</li></ul></div></div>
  </div>
</div>

<!-- connector -->
<svg class="connector" width="1200" height="3015" aria-hidden="true">
  <path d="M369,1294 V1398 H810 V1867 H367 V1918" fill="none" stroke="var(--lime)" stroke-width="1.6" stroke-dasharray="6 5"/>
</svg>

<!-- feature 1 -->
<div class="card" style="left:152px;top:961px"></div>
<div class="board board--white" style="left:98px;top:1029px;height:522px;transform:scale(0.505)">
  <div class="board__side"><span class="board__mark"></span><span class="board__icon board__icon--on" style="top:43px"></span><span class="board__icon" style="top:70px"></span><span class="board__icon" style="top:93px"></span><span class="board__avatar"></span></div>
  <div class="board__title">Entry</div>
  <div class="board__date">Wed Aug 21 2024 ⌄</div>
  <span class="pill" style="position:absolute;left:262px;top:39px;background:#2d3a55">Default Journal</span>
  <div class="col" style="left:125px;height:410px"><div class="col__head"><span class="col__icon"></span>What Went Well?</div><div class="col__editor"><div class="col__tools">Normal &nbsp;⇕ <b>B</b> <i>I</i> U S ”<br>☰ ☰ ☰ ☰ &nbsp;&nbsp;T</div><div class="col__body"></div></div></div>
  <div class="col" style="left:375px;height:410px"><div class="col__head"><span class="col__icon col__icon--tri"></span>What Didn't Go Well?</div><div class="col__editor"><div class="col__tools">Normal &nbsp;⇕ <b>B</b> <i>I</i> U S ”<br>☰ ☰ ☰ ☰ &nbsp;&nbsp;T</div><div class="col__body"></div></div></div>
  <div class="col" style="left:624px;height:410px"><div class="col__head"><span class="col__icon"></span>Things To Try</div><div class="col__editor"><div class="col__tools">Normal &nbsp;⇕ <b>B</b> <i>I</i> U S ”<br>☰ ☰ ☰ ☰ &nbsp;&nbsp;T</div><div class="col__body"></div></div></div>
</div>
<h2 class="feature-title" style="left:667px;top:983px">What Went Well</h2>
<span class="rule" style="left:676px;top:1048px"></span>
<p class="feature-text" style="left:676px;top:1070px">Sed ut perspiciatis unde omnis iste natus error sit voluptatem accusantium doloremque laudantium, totam rem aperiam, eaque ipsa quae ab illo inventore veritatis et quasi architecto beatae vitae dicta sunt explicabo. Nemo enim ipsam voluptatem quia voluptas sit aspernatur aut odit aut fugit,</p>

<!-- feature 2 -->
<h2 class="feature-title" style="left:98px;top:1459px">What Didn't Go Wel</h2>
<span class="rule" style="left:98px;top:1524px"></span>
<p class="feature-text" style="left:98px;top:1546px">Sed ut perspiciatis unde omnis iste natus error sit voluptatem accusantium doloremque laudantium, totam rem aperiam, eaque ipsa quae ab illo inventore veritatis et quasi architecto beatae vitae dicta sunt explicabo. Nemo enim ipsam voluptatem quia voluptas sit aspernatur aut odit aut fugit,</p>
<div class="card" style="left:588px;top:1438px"></div>
<div class="board board--white" style="left:633px;top:1506px;height:522px;transform:scale(0.509)">
  <div class="board__side"><span class="board__mark"></span><span class="board__icon board__icon--on" style="top:43px"></span><span class="board__icon" style="top:70px"></span><span class="board__icon" style="top:93px"></span><span class="board__avatar"></span></div>
  <div class="board__title">Entry</div>
  <div class="board__date">Thu Aug 22 2024 ⌄</div>
  <span class="pill board__tag">Gym</span>
  <div class="col" style="left:125px;height:410px"><div class="col__head"><span class="col__icon"></span>What Went Well?</div><div class="col__editor"><div class="col__tools">Normal &nbsp;⇕ <b>B</b> <i>I</i> U S ”<br>☰ ☰ ☰ ☰ &nbsp;&nbsp;T</div><div class="col__body"><ul><li>Completed all scheduled workouts this week.</li><li>Increased bench press weight by 10 pounds.</li><li>Maintained consistent energy levels throughout sessions.</li></ul></div></div></div>
  <div class="col" style="left:375px;height:410px"><div class="col__head"><span class="col__icon col__icon--tri"></span>What Didn't Go Well?</div><div class="col__editor"><div class="col__tools">Normal &nbsp;⇕ <b>B</b> <i>I</i> U S ”<br>☰ ☰ ☰ ☰ &nbsp;&nbsp;T</div><div class="col__body"><ul><li>Struggled with form on deadlifts, leading to lower back discomfort.</li><li>Missed two stretching sessions after workouts.</li><li>Skipped meal prep, resulting in inconsistent nutrition.</li></ul></div></div></div>
  <div class="col" style="left:624px;height:410px"><div class="col__head"><span class="col__icon"></span>Things To Try</div><div class="col__editor"><div class="col__tools">Normal &nbsp;⇕ <b>B</b> <i>I</i> U S ”<br>☰ ☰ ☰ ☰ &nbsp;&nbsp;T</div><div class="col__body"><ul><li>Focus on deadlift form by lowering the weight and reviewing proper technique.</li><li>Set reminders for post-workout stretching to prevent muscle tightness.</li><li>Dedicate Sunday evenings to meal prep to ensure a balanced diet.</li></ul></div></div></div>
</div>

<!-- feature 3 -->
<div class="card" style="left:152px;top:1918px"></div>
<div class="list-shot">
  <div class="side"><i style="top:28px"></i><i style="top:38px"></i><i style="top:48px"></i></div>
  <span class="add">+ Add New</span>
  <span class="pill gym">Gym</span>
  <div class="entry" style="top:50px;height:166px">
    <h4>Thu Aug 22 2024</h4>
    <em>What Went Well</em>
    Completed all scheduled workouts this week.<br>Increased bench press weight by 10 pounds.<br>Maintained consistent energy levels throughout sessions.
    <em>What Didn't Go Well</em>
    Struggled with form on deadlifts, leading to lower back discomfort.<br>Missed two stretching sessions after workouts.<br>Skipped meal prep, resulting in inconsistent nutrition.
    <em>Things To Try</em>
    Focus on deadlift form by lowering the weight and reviewing proper technique.<br>Set reminders for post-workout stretching to prevent muscle tightness.<br>Dedicate Sunday evenings to meal prep to ensure a balanced diet.
  </div>
  <div class="entry" style="top:224px;height:60px">
    <h4>Tue Aug 20 2024</h4>
    <em>What Went Well</em>
    Achieved a personal best in squats, adding 15 pounds.<br>Stayed consistent with cardio sessions.
  </div>
</div>
<h2 class="feature-title" style="left:666px;top:1941px">Things To Try</h2>
<span class="rule" style="left:666px;top:2005px"></span>
<p class="feature-text" style="left:666px;top:2027px">Sed ut perspiciatis unde omnis iste natus error sit voluptatem accusantium doloremque laudantium, totam rem aperiam, eaque ipsa quae ab illo inventore veritatis et quasi architecto beatae vitae dicta sunt explicabo. Nemo enim ipsam voluptatem quia voluptas sit aspernatur aut odit aut fugit,</p>

<!-- AI coach -->
<h2 class="ai-title">AI coach</h2>
<span class="rule" style="left:539px;top:2605px;width:106px"></span>
<p class="ai-text">Lorem ipsum dolor sit amet, consectetur adipiscing elit, sed do eiusmod tempor incididunt ut labore et dolore magna aliqua. Ut enim ad minim veniam, quis nostrud exercitation ullamco laboris nisi ut aliquip ex ea commodo consequat.</p>
<a class="btn" style="left:533px;top:2771px;width:133px;height:37px">Coming Soon</a>

<!-- footer -->
<div class="footer-line"></div>
<div class="logo" style="left:98px;top:2890px">Tavorly</div>
<span class="footer-nav" style="left:405px">Features</span>
<span class="footer-nav" style="left:553px">Solutions</span>
<span class="footer-nav" style="left:708px">Enterprise</span>
<span class="footer-nav" style="left:872px">Resources</span>
<span class="footer-nav" style="left:1035px">Pricing</span>
<p class="copyright">© copyrights 2024 &nbsp;Tavorly | &nbsp;All Rights Reserved</p>

</body>
</html>
```